Masonry and Landscaping Construction company business card

Looking for a business card design for a construction company named Ferrante Construction. It is an italian-american family business that specializes in custom stone work, patios, walkways, driveways, steps, outdoor kitchens, concrete, waterproofing, power wash, landscaping and more. Our colors are mostly red and white with some black. We're looking for a bold design. we also like to incorporate a picture of my family's hometown somewhere in it.
Target Market(s)
Luxury home owners
Industry/Entity Type
Construction
Contact Information for Business Card
Details includes should be bullet points mentioning the services provided. Custom Stone Work, Outdoor Kitchens, Fire Pits, Patios, Walkways, Steps, Concrete, Waterproofing, powerwash and landscaping
Requirements
Must have
- Would like a spot on the card for co-owners names, numbers and email to be listed also looking to add the QR code for an instagram page
Nice to have
- would like something bold, based around the colors red and white with black outlines or details

```html
<!DOCTYPE html>
<html lang="en">
<head>
<meta charset="utf-8">
<title>Ferrante Construction – Business Card</title>
<link rel="stylesheet" href="https://fonts.googleapis.com/css2?family=Ubuntu:wght@400;500;700&display=swap">
<style>
  :root {
    --bg: #3a3a3a;
    --card-white: #ffffff;
    --brand-red: #d7212a;
    --brand-red-soft: #e0444b;
    --brand-red-deep: #c22b30;
    --ink: #1a1a1a;
    --black: #0c0c0c;
  }
  * { margin: 0; padding: 0; box-sizing: border-box; }
  html, body {
    width: 1200px; height: 1059px; overflow: hidden;
    background: var(--bg);
    font-family: "Ubuntu", sans-serif;
  }
  .card {
    position: absolute;
    border-radius: 18px;
    overflow: hidden;
  }
  /* Front face */
  .card-front {
    left: 256px; top: 100px; width: 688px; height: 390px;
    background: var(--card-white);
  }
  .wordmark {
    position: absolute; left: 0; right: 0;
    text-align: center; font-weight: 700; line-height: 1;
  }
  .card-front .wordmark { top: 92px; color: var(--ink); }
  .wordmark-name { display: block; font-size: 58px; letter-spacing: 2px; }
  .wordmark-sub { display: block; font-size: 22px; letter-spacing: 7px; margin-top: 12px; }
  .owner {
    position: absolute; right: 377px; top: 270px; text-align: right;
  }
  .owner-name {
    color: var(--brand-red); font-weight: 500; font-size: 36px; line-height: 1;
    white-space: nowrap;
  }
  .owner-role {
    color: var(--ink); font-size: 21px; margin-top: 10px; line-height: 1;
  }
  .divider {
    position: absolute; left: 343px; top: 275px; width: 1.5px; height: 61px;
    background: var(--brand-red);
  }
  .contact {
    position: absolute; left: 380px; list-style: none;
  }
  .contact li {
    display: flex; align-items: center; height: 22px; margin-bottom: 12px;
    font-size: 21px; color: var(--ink);
  }
  .contact svg { width: 17px; height: 17px; margin-right: 16px; flex: none; }
  .contact { top: 275px; }
  .stripe-red {
    position: absolute; left: 0; bottom: 0; width: 343px; height: 17px;
    background: var(--brand-red);
  }
  .stripe-black {
    position: absolute; left: 346px; right: 0; bottom: 0; height: 17px;
    background: var(--black);
  }
  /* Back face */
  .card-back {
    left: 253px; top: 537px; width: 694px; height: 394px;
    background: var(--brand-red-deep);
  }
  .hometown-photo {
    position: absolute; inset: 0;
    background: linear-gradient(180deg, var(--brand-red-soft) 0%, #d2383e 40%, var(--brand-red-deep) 100%);
  }
  .card-back .wordmark { top: 138px; color: var(--card-white); }
  .services {
    position: absolute; left: 0; right: 0; top: 322px;
    text-align: center; color: var(--card-white);
    font-size: 16px; line-height: 22px; letter-spacing: 0.2px;
  }
</style>
</head>
<body>
  <section class="card card-front">
    <div class="wordmark">
      <span class="wordmark-name">FERRANTE</span>
      <span class="wordmark-sub">CONSTRUCTION</span>
    </div>
    <div class="owner">
      <p class="owner-name">MARCO RUSSO</p>
      <p class="owner-role">CO-OWNERS</p>
    </div>
    <div class="divider"></div>
    <ul class="contact">
      <li>
        <svg viewBox="0 0 24 24" aria-hidden="true"><path fill="none" stroke="#d7212a" stroke-width="2.2" stroke-linejoin="round" d="M5 3h4l2 5-2.5 1.5a11 11 0 0 0 6 6L16 13l5 2v4a2 2 0 0 1-2 2A16 16 0 0 1 3 5a2 2 0 0 1 2-2z"/></svg>
        (555)304-7182
      </li>
      <li>
        <svg viewBox="0 0 24 24" aria-hidden="true"><rect x="2" y="5" width="20" height="14" rx="1.5" fill="none" stroke="#d7212a" stroke-width="2.4"/><path d="M3 6l9 7 9-7" fill="none" stroke="#d7212a" stroke-width="2.4"/></svg>
        info@ferrantebuild.com
      </li>
    </ul>
    <div class="stripe-red"></div>
    <div class="stripe-black"></div>
  </section>

  <section class="card card-back">
    <div class="hometown-photo" role="img" aria-label="Red-tinted photograph of the family's Italian hometown with a bell tower and hillside"></div>
    <div class="wordmark">
      <span class="wordmark-name">FERRANTE</span>
      <span class="wordmark-sub">CONSTRUCTION</span>
    </div>
    <p class="services">CUSTOM STONE WORK, OUTDOOR KITCHENS, FIRE PITS, PATIOS, WALKWAYS,<br>STEPS, CONCRETE, WATERPROOFING, POWERWASH AND LANDSCAPING</p>
  </section>
</body>
</html>
```